Postcard Design Project

We are a small printing company specializing in envelope printing.
We market to churches and medical offices.

Industry/Entity Type

It Company

```html
<!DOCTYPE html>
<html lang="en">
<head>
<meta charset="utf-8">
<title>Halvern Printing – Postcard</title>
<link rel="stylesheet" href="https://fonts.googleapis.com/css2?family=Oswald:wght@500;700&family=Source+Sans+3:wght@400;600&display=swap">
<style>
  :root {
    --paper: #e9f2fa;
    --brick: #961b1f;
    --airmail-blue: #0055a5;
    --sun: #fff200;
    --white: #ffffff;
  }
  * { margin: 0; padding: 0; box-sizing: border-box; }
  html, body { width: 1200px; height: 816px; overflow: hidden; background: var(--paper); }
  .postcard {
    position: relative;
    width: 1200px;
    height: 816px;
    background: var(--paper);
    overflow: hidden;
  }
  .postcard__art { position: absolute; inset: 0; width: 1200px; height: 816px; }
  .stripe--red { fill: var(--brick); }
  .stripe--blue { fill: var(--airmail-blue); }
  .brand-tab, .estimate-band, .stamp-box__frame { fill: var(--brick); }
  .stamp-box__hole { fill: var(--paper); }
  .stamp-box__perf { fill: var(--white); }
  .divider, .address-line { stroke: var(--brick); stroke-width: 1.6; }

  .brand-name {
    position: absolute;
    left: 155px; top: 70px; width: 304px;
    text-align: center;
    font-family: 'Oswald', sans-serif;
    font-weight: 700;
    color: var(--sun);
    line-height: 1;
  }
  .brand-name__main { display: block; font-size: 74px; letter-spacing: 1px; }
  .brand-name__sub { display: block; font-size: 42px; letter-spacing: 3px; margin-top: 6px; }

  .intro {
    position: absolute;
    left: 122px; top: 334px; width: 372px;
    font-family: 'Source Sans 3', sans-serif;
    font-weight: 400;
    font-size: 23px;
    line-height: 32px;
    color: var(--brick);
    text-align: justify;
    text-align-last: center;
  }

  .estimate {
    position: absolute;
    left: 48px; top: 528px; width: 522px;
    text-align: center;
    font-family: 'Oswald', sans-serif;
    font-weight: 700;
    color: var(--sun);
    line-height: 1;
  }
  .estimate__label { display: block; font-size: 37px; margin-top: 6px; }
  .estimate__phone { display: block; font-size: 55px; margin-top: 4px; letter-spacing: 1px; }

  .email {
    position: absolute;
    left: 48px; top: 708px; width: 522px;
    text-align: center;
    font-family: 'Source Sans 3', sans-serif;
    font-weight: 600;
    font-size: 31px;
    letter-spacing: 5.5px;
    color: var(--brick);
  }
</style>
</head>
<body>
<main class="postcard">
  <svg class="postcard__art" viewBox="0 0 1300 884" aria-hidden="true">
    <defs>
      <clipPath id="message-side"><rect x="0" y="0" width="650" height="884"/></clipPath>
    </defs>

    <g clip-path="url(#message-side)">
      <!-- top airmail border -->
      <polygon class="stripe--red"  points="42,52 68,0 148,0 122,52"/>
      <polygon class="stripe--blue" points="166,52 192,0 272,0 246,52"/>
      <polygon class="stripe--red"  points="292,52 318,0 398,0 372,52"/>
      <polygon class="stripe--blue" points="418,52 444,0 524,0 498,52"/>
      <polygon class="stripe--red"  points="544,52 570,0 650,0 650,52"/>

      <!-- bottom airmail border -->
      <polygon class="stripe--red"  points="68,884 94,832 174,832 148,884"/>
      <polygon class="stripe--blue" points="188,884 214,832 294,832 268,884"/>
      <polygon class="stripe--red"  points="308,884 334,832 414,832 388,884"/>
      <polygon class="stripe--blue" points="428,884 454,832 534,832 508,884"/>
      <polygon class="stripe--red"  points="548,884 574,832 654,832 628,884"/>
    </g>

    <!-- left airmail border -->
    <polygon class="stripe--blue" points="0,55 52,80 52,160 0,135"/>
    <polygon class="stripe--red"  points="0,170 52,195 52,275 0,250"/>
    <polygon class="stripe--blue" points="0,287 52,312 52,392 0,367"/>
    <polygon class="stripe--red"  points="0,403 52,428 52,508 0,483"/>
    <polygon class="stripe--blue" points="0,520 52,545 52,625 0,600"/>
    <polygon class="stripe--red"  points="0,637 52,662 52,742 0,717"/>
    <polygon class="stripe--blue" points="0,752 52,777 52,857 0,832"/>

    <!-- brand tab -->
    <path class="brand-tab" d="M168,52 H497 V190 A90,90 0 0 1 407,280 H258 A90,90 0 0 1 168,190 Z"/>

    <!-- estimate band -->
    <polygon class="estimate-band" points="52,572 650,572 602,697 52,697"/>

    <!-- centre divider -->
    <line class="divider" x1="650" y1="0" x2="650" y2="884"/>

    <!-- stamp box -->
    <g class="stamp-box">
      <rect class="stamp-box__frame" x="1125" y="52" width="123" height="132"/>
      <rect class="stamp-box__hole" x="1140" y="67" width="93" height="102"/>
      <g class="stamp-box__perf">
        <circle cx="1125" cy="72" r="5"/><circle cx="1125" cy="96" r="5"/><circle cx="1125" cy="118" r="5"/><circle cx="1125" cy="140" r="5"/><circle cx="1125" cy="162" r="5"/>
        <circle cx="1248" cy="72" r="5"/><circle cx="1248" cy="96" r="5"/><circle cx="1248" cy="118" r="5"/><circle cx="1248" cy="140" r="5"/><circle cx="1248" cy="162" r="5"/>
        <circle cx="1145" cy="52" r="5"/><circle cx="1167" cy="52" r="5"/><circle cx="1189" cy="52" r="5"/><circle cx="1211" cy="52" r="5"/><circle cx="1232" cy="52" r="5"/>
        <circle cx="1145" cy="184" r="5"/><circle cx="1167" cy="184" r="5"/><circle cx="1189" cy="184" r="5"/><circle cx="1211" cy="184" r="5"/><circle cx="1232" cy="184" r="5"/>
      </g>
    </g>

    <!-- address lines -->
    <line class="address-line" x1="748" y1="554" x2="1182" y2="554"/>
    <line class="address-line" x1="748" y1="615" x2="1182" y2="615"/>
    <line class="address-line" x1="748" y1="676" x2="1182" y2="676"/>
    <line class="address-line" x1="748" y1="737" x2="1182" y2="737"/>
  </svg>

  <h1 class="brand-name">
    <span class="brand-name__main">HALVERN</span>
    <span class="brand-name__sub">PRINTING</span>
  </h1>

  <p class="intro">Lorem ipsum dolor sit amet, consectetur adipiscing elit, sed do eiusmod tempor incididunt ut labore et dolore magna aliqua.</p>

  <p class="estimate">
    <span class="estimate__label">Call for a free estimate</span>
    <span class="estimate__phone">626-555-0148</span>
  </p>

  <p class="email">hello@halvernprint.com</p>
</main>
</body>
</html>
```